International emerging specialist Research and Development Company focused on plant-based medicine

We need a powerpoint design for a new company based in British Columbia, Canada called Tovel Phytrix. We are focused on developing plant-based medicines. The company is driven by its experience in research and development work in plant genetics, cultivation techniques, natural medicines, biochemistry, agriculture and technologies. Tovel will research, develop and produce very unique and specific cultivars from the plant kingdom needed for specific ailments in medical patients. We would like to see designs that use our current logo and its colour scheme. The final design should communicate financial safety, growth, and research and development.

```html
<!DOCTYPE html>
<html lang="en">
<head>
<meta charset="utf-8">
<title>Tovel Phytrix – Presentation Template</title>
<link rel="stylesheet" href="https://fonts.googleapis.com/css2?family=PT+Sans:ital,wght@0,400;0,700;1,400&family=PT+Sans+Narrow:wght@400;700&display=swap">
<style>
  :root{
    --stage:#2b2e31;
    --brand-red:#e0232a;
    --brand-red-dark:#b3141a;
    --title-red:#8a0f14;
    --slate:#4a4a4c;
    --paper:#f1f1f1;
    --blush:#fbe9ea;
    --ink:#3a3a3a;
    --white:#ffffff;
  }
  *{margin:0;padding:0;box-sizing:border-box}
  html,body{width:1200px;height:1000px;overflow:hidden;background:var(--stage)}
  .deck{position:relative;width:1200px;height:1000px}
  .slide{position:absolute;width:588px;height:440px;overflow:hidden;background:var(--paper);box-shadow:0 2px 8px rgba(0,0,0,.6)}
  .slide--cover{left:8px;top:55px;background:var(--slate)}
  .slide--blank{left:605px;top:55px}
  .slide--about{left:8px;top:505px}
  .slide--network{left:605px;top:505px}
  .slide__backdrop{position:absolute;inset:0}

  /* cover */
  .cover__date{position:absolute;right:38px;top:17px;font:400 13px "PT Sans Narrow",sans-serif;color:#e8e8e8}
  .cover__brand{position:absolute;left:135px;top:180px;display:flex;align-items:center;gap:14px}
  .brand-dot{width:34px;height:34px;border-radius:50%;background:var(--brand-red)}
  .cover__brand .brand-name{font:700 58px "PT Sans",sans-serif;color:var(--white);letter-spacing:-1px}
  .cover__title{position:absolute;right:38px;top:336px;font:700 31px "PT Sans Narrow",sans-serif;color:#f2f2f2}
  .cover__sub{position:absolute;right:38px;top:380px;width:330px;text-align:right;font:400 12.5px/18px "PT Sans Narrow",sans-serif;color:#e0e0e0}

  /* content slides */
  .slide__flag{position:absolute;left:0;top:12px}
  .slide__title{position:absolute;left:28px;top:10px;font:700 26px "PT Sans Narrow",sans-serif;color:var(--title-red)}
  .watermark{position:absolute;left:130px;top:175px;font:700 86px "PT Sans",sans-serif;color:rgba(255,255,255,.75);letter-spacing:-2px}
  .corner-brand{position:absolute;right:22px;top:335px;display:flex;align-items:center;gap:8px}
  .corner-brand .brand-dot{width:20px;height:20px}
  .corner-brand .brand-name{font:700 30px "PT Sans",sans-serif;color:var(--slate);letter-spacing:-.5px}
  .slide__footer{position:absolute;left:0;bottom:0;width:100%;height:44px;background:linear-gradient(var(--brand-red),var(--brand-red-dark));border-top:2px solid #c01a20;display:flex;align-items:center;padding:0 14px 0 20px}
  .footer__caption{flex:1;font:italic 400 13.5px "PT Sans",sans-serif;color:var(--white)}
  .nav-btn{margin-left:8px;padding:5px 11px;font:400 13px "PT Sans",sans-serif;color:var(--white);background:#a81318;border-radius:4px;box-shadow:inset 0 1px 0 rgba(255,255,255,.2),0 1px 2px rgba(0,0,0,.4)}

  .section-head{position:absolute;left:43px;top:72px;font:700 17px "PT Sans Narrow",sans-serif;color:var(--title-red)}
  .ticks{position:absolute;left:44px;top:100px;list-style:none;font:400 12.5px/19px "PT Sans Narrow",sans-serif;color:var(--ink)}
  .ticks li{position:relative;padding-left:22px}
  .ticks li::before{content:"";position:absolute;left:3px;top:3px;width:6px;height:11px;border:solid var(--brand-red-dark);border-width:0 3px 3px 0;transform:rotate(40deg)}
  .slide--about .ticks{width:480px}
  .team-photo{position:absolute;left:212px;top:95px;width:350px;height:290px;background:linear-gradient(180deg,#4a4d55 0%,#6b6e75 55%,rgba(241,241,241,0) 100%);border-radius:4px}
</style>
</head>
<body>
<main class="deck">

  <section class="slide slide--cover">
    <svg class="slide__backdrop" width="588" height="440" viewBox="0 0 588 440" aria-hidden="true">
      <path d="M0 0 H175 C160 60 180 110 168 170 C155 240 178 320 165 440 H0 Z" fill="var(--brand-red)" stroke="#ffffff" stroke-width="4"/>
    </svg>
    <p class="cover__date">31 Desember 2015</p>
    <div class="cover__brand"><span class="brand-dot"></span><span class="brand-name">Tovel Phytrix</span></div>
    <h1 class="cover__title">Project Title Here</h1>
    <p class="cover__sub">Subtext here Subtext here Subtext here Subtext here Subtext here Subtext here Subtext here Subtext here</p>
  </section>

  <section class="slide slide--blank">
    <svg class="slide__backdrop" width="588" height="440" viewBox="0 0 588 440" aria-hidden="true">
      <path d="M0 0 H175 C160 60 180 110 168 170 C155 240 178 320 165 440 H0 Z" fill="var(--blush)"/>
    </svg>
    <svg class="slide__flag" width="24" height="30" viewBox="0 0 24 30" aria-hidden="true"><path d="M0 0 H22 V30 H0 L10 15 Z" fill="var(--brand-red-dark)"/></svg>
    <h2 class="slide__title">Slide Title Presentation</h2>
    <p class="watermark">Tovel Phytrix</p>
    <div class="corner-brand"><span class="brand-dot"></span><span class="brand-name">Tovel Phytrix</span></div>
    <footer class="slide__footer"><span class="footer__caption">Timeline about your Slide Presentation</span><span class="nav-btn">Back</span><span class="nav-btn">Next</span></footer>
  </section>

  <section class="slide slide--about">
    <svg class="slide__backdrop" width="588" height="440" viewBox="0 0 588 440" aria-hidden="true">
      <path d="M0 0 H175 C160 60 180 110 168 170 C155 240 178 320 165 440 H0 Z" fill="var(--blush)"/>
    </svg>
    <svg class="slide__flag" width="24" height="30" viewBox="0 0 24 30" aria-hidden="true"><path d="M0 0 H22 V30 H0 L10 15 Z" fill="var(--brand-red-dark)"/></svg>
    <h2 class="slide__title">Slide Title Presentation</h2>
    <h3 class="section-head">Harbor Modern Real Estate</h3>
    <ul class="ticks">
      <li>High volume local boutique real estate company</li>
      <li>Specialize in selling homes throughout the San Francisco Bay Area</li>
      <li>Focus on modern marketing techniques and thinking outside the box</li>
      <li>“High Tech and High Touch” approach to real estate</li>
      <li>Certified Green Business Everything is done and stored online. No File Cabinets in our offices!</li>
      <li>Exceptional web presence far beyond other local real estate companies</li>
      <li>Clean, streamline, and hip marketing materials</li>
      <li>A company constantly looking into the latest real estate trends, tools, and technology to better assist their agents and clients sell homes in the modern world, all while embracing tried and true real estate values and practices as well</li>
      <li>Leading authority for architectural homes and recognized world wide</li>
      <li>Not Just Modern Homes! We focus on Modern Real Estate Practices through and through.</li>
    </ul>
    <div class="corner-brand"><span class="brand-dot"></span><span class="brand-name">Tovel Phytrix</span></div>
    <footer class="slide__footer"><span class="footer__caption">Timeline about your Slide Presentation</span><span class="nav-btn">Back</span><span class="nav-btn">Next</span></footer>
  </section>

  <section class="slide slide--network">
    <svg class="slide__backdrop" width="588" height="440" viewBox="0 0 588 440" aria-hidden="true">
      <path d="M0 0 H175 C160 60 180 110 168 170 C155 240 178 320 165 440 H0 Z" fill="var(--blush)"/>
    </svg>
    <svg class="slide__flag" width="24" height="30" viewBox="0 0 24 30" aria-hidden="true"><path d="M0 0 H22 V30 H0 L10 15 Z" fill="var(--brand-red-dark)"/></svg>
    <h2 class="slide__title">Slide Title Presentation</h2>
    <h3 class="section-head">I’ve got connections!</h3>
    <ul class="ticks">
      <li>Handymen</li>
      <li>Contractors</li>
      <li>Stagers</li>
      <li>Painters</li>
      <li>Cleaners</li>
      <li>Movers</li>
      <li>Storage companies</li>
      <li>Landscapers</li>
      <li>Estate Sale Professionals</li>
      <li>Lawyers</li>
      <li>Mortgage Brokers</li>
      <li>Inspectors</li>
    </ul>
    <div class="team-photo" role="img" aria-label="Group photo of business professionals and tradespeople standing together"></div>
    <div class="corner-brand"><span class="brand-dot"></span><span class="brand-name">Tovel Phytrix</span></div>
    <footer class="slide__footer"><span class="footer__caption">Timeline about your Slide Presentation</span><span class="nav-btn">Back</span><span class="nav-btn">Next</span></footer>
  </section>

</main>
</body>
</html>
```